A revolutionary website for a revolutionary construction company

I am looking for inspirations... please help me and read the attached brief

I would like to achieve a website design that is modern, premium dynamic and drives emotions. I do not want a design that can be found on a normal template. Having that said, I would also like the utilisation of Illustrations that are relation to the company’s services…. Also would like to have illustrations dynamic when you navigate on them. So a young, dynamic and parallax design website that will show off these requirements. Also to add trust, with all pages designed.

please see attachements.
Updates

Low design quality

Target Market(s)

Please read brief

Number of Pages Required

5+ page

Font styles to use
Other font styles liked:
• Futura

Requirements
Must have
• Please read brief - colours to be matching logo colours
Nice to have
Should not have

```html
<!DOCTYPE html>
<html lang="en">
<head>
<meta charset="utf-8">
<title>KVR Steel</title>
<link rel="stylesheet" href="https://fonts.googleapis.com/css2?family=Montserrat:wght@500;600;700;800&family=Raleway:ital,wght@0,400;0,500;1,400&family=Roboto+Slab:wght@400&display=swap">
<style>
:root{
  --orange:#f24a12;
  --navy:#1a2646;
  --ink:#1b1f2e;
  --text:#555b66;
  --white:#ffffff;
  --bg:#f6f6f7;
}
*{margin:0;padding:0;box-sizing:border-box}
html,body{width:1200px;height:3383px;overflow:hidden}
body{position:relative;background:var(--bg);font-family:"Raleway",sans-serif;color:var(--ink)}
.abs{position:absolute}

/* header */
.site-header{left:0;top:0;width:1200px;height:118px;background:var(--white);z-index:3}
.brand{left:115px;top:38px;display:flex;align-items:center;gap:12px;font-family:"Montserrat",sans-serif;font-weight:800;font-size:38px;color:var(--ink);letter-spacing:1px;line-height:1}
.brand-dot{width:28px;height:28px;border-radius:50%;background:var(--orange)}
.nav-link{top:58px;font-size:15.5px;font-weight:500;color:#222;text-decoration:none;white-space:nowrap;line-height:20px}
.nav-link.active{color:var(--orange)}

/* hero */
.hero-photo{left:0;top:118px;width:1200px;height:660px;
  background:
    radial-gradient(ellipse 260px 160px at 1000px 170px,rgba(210,60,45,.75),transparent 70%),
    radial-gradient(ellipse 300px 140px at 700px 120px,rgba(190,55,40,.55),transparent 70%),
    radial-gradient(ellipse 200px 180px at 170px 160px,rgba(230,110,60,.45),transparent 70%),
    radial-gradient(ellipse 500px 220px at 650px 560px,rgba(10,14,22,.85),transparent 70%),
    linear-gradient(180deg,#4b5868 0%,#3a3f4c 40%,#283344 65%,#141b27 100%);
  clip-path:path("M0 0H1200V565Q600 745 0 565Z")}
.hero-wave{left:0;top:118px}
.hero-title{left:115px;top:302px;font-family:"Montserrat",sans-serif;font-weight:700;font-size:110px;color:var(--white);letter-spacing:-3px;line-height:1}
.hero-sub{left:113px;top:415px;width:560px;color:var(--white);font-size:18.5px;line-height:34px}
.btn{display:flex;align-items:center;justify-content:center;background:var(--orange);color:var(--white);border-radius:26px;font-family:"Roboto Slab",serif;font-size:16px;text-decoration:none;box-shadow:0 3px 8px rgba(0,0,0,.2)}
.hero-btn{left:110px;top:495px;width:154px;height:50px}

/* products */
.section-title{left:0;width:1200px;text-align:center;font-family:"Montserrat",sans-serif;font-weight:700;font-size:42px;color:var(--ink);letter-spacing:-.5px;line-height:50px}
.section-title .accent{color:var(--orange)}
.product{width:318px;height:359px;top:929px;overflow:hidden}
.product-label{top:1307px;width:318px;text-align:center;font-family:"Roboto Slab",serif;font-size:20px;color:#2a2a2a;letter-spacing:.5px}
.product-overlay{left:0;top:0;width:318px;height:359px;padding:96px 18px 0;text-align:center;color:var(--white);font-size:13.5px;line-height:31px}
.product-overlay a{display:block;margin-top:9px;color:var(--orange);font-family:"Roboto Slab",serif;font-size:15px;text-decoration:underline}

/* about */
.about-photo{left:0;top:1435px;width:1200px;height:508px;
  background:
    radial-gradient(ellipse 180px 260px at 1000px 250px,rgba(30,34,40,.75),transparent 70%),
    radial-gradient(ellipse 120px 180px at 770px 360px,rgba(30,34,40,.7),transparent 70%),
    radial-gradient(ellipse 140px 140px at 590px 280px,rgba(220,225,235,.7),transparent 70%),
    linear-gradient(180deg,#5d86b8 0%,#8eaed2 50%,#7c93ab 80%,#5e6b7a 100%)}
.about-card{left:86px;top:1464px;width:410px;height:453px;background:var(--white);padding:52px 28px 0 26px}
.about-card h2{font-family:"Montserrat",sans-serif;font-weight:700;font-size:33px;color:var(--ink);letter-spacing:-.3px;line-height:40px}
.about-card h2 span{color:var(--orange)}
.about-card p{margin-top:18px;font-size:13px;line-height:31px;color:var(--text);text-align:justify}
.about-btn{left:110px;top:1805px;width:154px;height:50px}

/* testimonials */
.quote{left:125px;top:2106px;width:950px;text-align:center;font-style:italic;font-size:15.5px;line-height:34px;color:#5d6270}
.quote-mark{font-family:Georgia,serif;font-size:40px;line-height:0;color:#c8cbd2;font-style:normal;vertical-align:-6px}
.quote-author{left:0;top:2219px;width:1200px;text-align:center;font-family:"Roboto Slab",serif;font-size:15px;color:#333;line-height:20px}
.round-arrow{width:40px;height:40px}

/* video */
.footer-band{left:0;top:2843px;width:1200px;height:540px;background:var(--navy)}
.video{left:110px;top:2419px;width:978px;height:568px;
  background:
    radial-gradient(ellipse 300px 80px at 250px 70px,rgba(170,175,185,.55),transparent 70%),
    radial-gradient(ellipse 350px 70px at 700px 290px,rgba(180,185,195,.5),transparent 70%),
    radial-gradient(ellipse 420px 80px at 300px 480px,rgba(150,80,45,.6),transparent 70%),
    linear-gradient(180deg,#53575d 0%,#3b342d 30%,#5c4a3a 55%,#3a3631 75%,#2b2826 100%)}
.video-caption{left:146px;top:2926px;font-family:"Montserrat",sans-serif;font-weight:600;font-size:15px;color:var(--white);line-height:20px}
.video-brand{left:146px;top:2460px;font-family:"Montserrat",sans-serif;font-weight:800;font-size:26px;color:var(--white);line-height:1}

/* footer */
.footer-col{top:3042px;color:var(--white)}
.footer-col h3{font-family:"Montserrat",sans-serif;font-weight:700;font-size:20px;line-height:26px;margin-bottom:16px}
.footer-col p{font-size:13.5px;line-height:28px;text-align:justify}
.footer-col ul{list-style:none;font-size:13.5px;line-height:34px}
.footer-col li{display:flex;align-items:center;gap:7px}
.socials{left:112px;top:3344px;display:flex;gap:10px}
.socials span{width:14px;height:14px;border-radius:50%;background:var(--white)}
.copyright{left:0;top:3342px;width:1200px;text-align:center;font-size:14px;color:var(--white);font-family:"Roboto Slab",serif}
</style>
</head>
<body>

<header class="site-header abs">
  <div class="brand abs"><span class="brand-dot"></span>KVR</div>
  <a class="nav-link active abs" style="left:410px">HOME</a>
  <a class="nav-link abs" style="left:488px">ABOUT</a>
  <a class="nav-link abs" style="left:574px">PRODUCTS</a>
  <a class="nav-link abs" style="left:687px">VIDEOS</a>
  <a class="nav-link abs" style="left:776px">TESTIMONIALS</a>
  <a class="nav-link abs" style="left:916px">CONTACT</a>
  <a class="nav-link abs" style="left:1017px;display:flex;align-items:center;gap:5px">
    <svg width="14" height="15" viewBox="0 0 14 15"><circle cx="7" cy="4.5" r="3.5" fill="none" stroke="#f24a12" stroke-width="1.5"/><path d="M1 14.5c0-3.5 2.7-5.5 6-5.5s6 2 6 5.5" fill="none" stroke="#f24a12" stroke-width="1.5"/></svg>LOGIN</a>
</header>

<section class="hero">
  <div class="hero-photo abs" role="img" aria-label="Steel pipe mill interior with long rows of stacked pipes under overhead cranes and red wall panels"></div>
  <svg class="hero-wave abs" width="1200" height="680" viewBox="0 0 1200 680">
    <path d="M0 572Q600 770 1200 572V590Q600 752 0 590Z" fill="var(--orange)"/>
  </svg>
  <div class="hero-title abs">KVR</div>
  <div class="hero-sub abs">Nemo enim ipsam voluptatem quia voluptas sit aspernatur<br>aut odit aut fugit,ratione voluptatem sequi nesciunt</div>
  <a class="btn hero-btn abs">GET STARTED</a>
  <svg class="abs" style="left:93px;top:420px" width="16" height="26" viewBox="0 0 16 26"><path d="M13 2L3 13l10 11" fill="none" stroke="#fff" stroke-width="3"/></svg>
  <svg class="abs" style="left:1092px;top:420px" width="16" height="26" viewBox="0 0 16 26"><path d="M3 2l10 11L3 24" fill="none" stroke="#fff" stroke-width="3"/></svg>
</section>

<section class="products">
  <h2 class="section-title abs" style="top:862px"><span class="accent">OUR</span> PRODUCTS</h2>
  <svg class="abs" style="left:86px;top:1116px" width="14" height="24" viewBox="0 0 14 24"><path d="M11 2L3 12l8 10" fill="none" stroke="#222" stroke-width="2.5"/></svg>
  <svg class="abs" style="left:1099px;top:1116px" width="14" height="24" viewBox="0 0 14 24"><path d="M3 2l8 10-8 10" fill="none" stroke="#222" stroke-width="2.5"/></svg>

  <div class="product abs" style="left:110px;background:radial-gradient(ellipse 200px 120px at 160px 120px,#e4e7ec,transparent 70%),radial-gradient(ellipse 220px 90px at 170px 300px,#d6dade,transparent 70%),linear-gradient(160deg,#b9c0c9,#7f8a97 50%,#4c5664)" role="img" aria-label="Stacks of longitudinal welded steel pipes in a warehouse"></div>
  <div class="product abs" style="left:440px;background:radial-gradient(ellipse 140px 100px at 60px 300px,rgba(120,40,25,.6),transparent 70%),radial-gradient(ellipse 140px 100px at 260px 230px,rgba(110,35,20,.5),transparent 70%),linear-gradient(160deg,#2a2421,#1a1716 60%,#2c1f1b)" role="img" aria-label="Welded pipe ends under a dark overlay">
    <div class="product-overlay abs">Nemo enim ipsam voluptatem quia voluptas sit aspernatur aut odit aut fugit, sed quia consequuntur magni dolores eos qui ratione voluptatem sequi nesciunt.<a>VIEW SPECIFICATION</a></div>
  </div>
  <div class="product abs" style="left:770px;background:radial-gradient(ellipse 150px 80px at 180px 80px,#c9c7c2,transparent 70%),radial-gradient(ellipse 60px 80px at 60px 60px,#8a6a48,transparent 70%),radial-gradient(ellipse 220px 100px at 150px 250px,#a9adb3,transparent 70%),linear-gradient(180deg,#7a6d5f 0%,#9a9ca1 45%,#5d6168 100%)" role="img" aria-label="Flat rolled steel coils and sheets on warehouse racks"></div>
  <div class="product-label abs" style="left:110px">LSAW PIPE</div>
  <div class="product-label abs" style="left:440px">ERW PIPE</div>
  <div class="product-label abs" style="left:770px">FLAT ROLLED</div>
</section>

<section class="about">
  <div class="about-photo abs" role="img" aria-label="Bundles of steel tube ends stacked against a blue sky"></div>
  <div class="about-card abs">
    <h2>ABOUT <span>US</span></h2>
    <p>Nemo enim ipsam voluptatem quia voluptas sit aspernatur aut odit aut fugit, sed quia consequuntur magni dolores eos qui ratione voluptatem sequi nesciunt. Neque porro quisquam est, qui dolorem ipsum quia dolor sit amet, consectetur, adipisci velit, sed quia non numquam eius modi tempora incidunt ut labore et dolore magnam aliquam quaerat voluptatem.</p>
  </div>
  <a class="btn about-btn abs">READ MORE</a>
</section>

<section class="testimonials">
  <h2 class="section-title abs" style="top:2037px">TESTIMONIALS</h2>
  <p class="quote abs"><span class="quote-mark">&ldquo;</span>Nemo enim ipsam voluptatem quia voluptas sit aspernatur aut odit aut fugit, sed quia consequuntur magni dolores eos qui ratione voluptatem sequi nesciunt. Neque porro quisquam est, qui dolorem ipsum quia dolor sit amet, consectetur, adipisci velit, sed quia non numquam eius modi tempora incidunt ut labore et dolore magnam aliquam quaerat voluptatem.<span class="quote-mark">&rdquo;</span></p>
  <div class="quote-author abs">- Mara Quinn</div>
  <svg class="round-arrow abs" style="left:50px;top:2125px" viewBox="0 0 40 40"><circle cx="20" cy="20" r="20" fill="var(--navy)"/><path d="M27 20H13m6-6l-6 6 6 6" fill="none" stroke="#fff" stroke-width="2.5"/></svg>
  <svg class="round-arrow abs" style="left:1109px;top:2125px" viewBox="0 0 40 40"><circle cx="20" cy="20" r="20" fill="var(--navy)"/><path d="M13 20h14m-6-6l6 6-6 6" fill="none" stroke="#fff" stroke-width="2.5"/></svg>
</section>

<section class="video-section">
  <h2 class="section-title abs" style="top:2335px">OUR <span class="accent">VIDEO</span></h2>
  <div class="footer-band abs"></div>
  <div class="video abs" role="img" aria-label="Video still of steel pipe racks in an open storage shed"></div>
  <div class="video-brand abs">KVR</div>
  <svg class="abs" style="left:538px;top:2643px" width="124" height="124" viewBox="0 0 124 124"><circle cx="62" cy="62" r="62" fill="var(--orange)" opacity=".55"/><circle cx="62" cy="62" r="50" fill="var(--orange)"/><path d="M50 42v40l34-20z" fill="#fff"/></svg>
  <div class="video-caption abs">LOREM IPSUM DOLOR SIT AMET, CONSECTETUR ADIPISCING ELIT</div>
</section>

<footer>
  <div class="footer-col abs" style="left:111px;width:270px">
    <h3>ABOUT US</h3>
    <p>Nemo enim ipsam voluptatem quia voluptas sit aspernatur aut odit aut fugit, sed quia consequuntur magni dolores eos qui ratione voluptatem sequi nesciunt. Neque porro quisquam est, qui dolorem ipsum quia dolor sit amet,</p>
  </div>
  <div class="footer-col abs" style="left:451px">
    <h3>QUICK LINKS</h3>
    <ul><li>Home</li><li>About</li><li>Products</li><li>Videos</li><li>Testimonials</li><li>Contact</li></ul>
  </div>
  <div class="footer-col abs" style="left:649px;width:250px">
    <h3>CONTACT US</h3>
    <ul style="line-height:38px">
      <li><svg width="11" height="11" viewBox="0 0 11 11"><path d="M2 0l2 3-1 1.5c.8 1.5 2 2.7 3.5 3.5L8 7l3 2-1 2C5 11 0 6 0 1z" fill="#fff"/></svg>Call - 888-888-8888</li>
      <li><svg width="12" height="10" viewBox="0 0 12 10"><rect x=".7" y=".7" width="10.6" height="8.6" fill="none" stroke="#fff" stroke-width="1.4"/><path d="M1 1l5 4 5-4" fill="none" stroke="#fff" stroke-width="1.4"/></svg>Email - info@kvrsteel.com</li>
      <li><svg width="10" height="13" viewBox="0 0 10 13"><path d="M5 0a5 5 0 0 1 5 5c0 3-5 8-5 8S0 8 0 5a5 5 0 0 1 5-5z" fill="#fff"/><circle cx="5" cy="5" r="1.8" fill="#1a2646"/></svg>Address - Nemo voluptatem quia</li>
      <li>voluptas sit</li>
    </ul>
  </div>
  <div class="footer-col abs" style="left:959px">
    <h3>HELP US</h3>
    <ul><li>Conatct</li><li>Terms &amp; Services</li><li>About Us</li></ul>
  </div>
  <div class="socials abs"><span></span><span></span><span></span></div>
  <div class="copyright abs">&copy; 2020 All Rights Reserved</div>
</footer>

</body>
</html>
```